依頼詳細
キービジュアルは綿帽子の女性写真と狐面。狐面を手に持っていても良いし、背後に入れても良い。

入れてくどくなければ入れたいのは、狐火(火の玉12個)・赤い番傘。

問合せ電話・チケット申込サイトは開設中。
記載項目
メインタイトル
(大きな筆文字・縦書き) 星のまたたき公演

キャッチコピー
(小さな筆文字・縦書き)
狐の嫁入り・鷺娘 など
桜綾音プロデュース
伝統芸能×障害者の美意識が融合する夢幻舞台
1000年続く四天王寺39代目による平安時代の和琴、時空を超えるほら貝、謎の語り部、妖艶日本舞踊・元歌舞伎役者の粋!狐行列は素敵な障害者たち!

テキスト
緑町公会堂
2023年11月25日(土)
17時~19時(開場16時半)
VIP席10000円・一般席当日受付7000円・一般席前売6000円
チケット申込QRコード○○○○
チケット申込TEL○○○

主催 一般社団法人 森のこだま
共催 一般社団法人 ハッピーステップ俱楽部
出演 桜綾音・藤波流清舟・村瀬健吾・KAZMO・紗弥・ハッピーステップ俱楽部(松田凛・
北川原誠一・石塚美穂・原田翔・大西菜摘・桑原陽斗・長谷部千尋・川口結衣・三浦彩乃・柴田浩明・吉川みき・堀江ナオ)
サイズ
A4
ページ数
片面
希望イメージ
シンプル 複雑
単色 カラフル
暗い 明るい
日常 高級
遊び心 厳粛
未来的 伝統的
女性的 男性的
希望する色
背景色はお任せします。詳細は添付テキストをご参照ください。
納品ファイル
補足説明
入校先は若葉カラー印刷 https://www.wkbp-print.jp/links/question/4-5

```html
<!DOCTYPE html>
<html lang="ja">
<head>
<meta charset="utf-8">
<title>星のまたたき公演</title>
<link rel="stylesheet" href="https://fonts.googleapis.com/css2?family=Yuji+Syuku&family=Shippori+Mincho:wght@500;700;800&display=swap">
<style>
  :root {
    --ink: #1b2740;
    --ink-soft: #3a4760;
    --teal: #2d5b76;
    --paper: #eef1f4;
    --mist: #c9d3dc;
    --night-top: #3e5266;
    --night-mid: #6f8497;
    --white: #ffffff;
  }
  html, body {
    margin: 0;
    padding: 0;
    width: 849px;
    height: 1200px;
    overflow: hidden;
    background: var(--paper);
  }
  .poster {
    position: relative;
    width: 849px;
    height: 1200px;
    overflow: hidden;
    background: var(--paper);
    font-family: "Shippori Mincho", serif;
    color: var(--ink);
  }
  .key-visual {
    position: absolute;
    left: 0; top: 0;
    width: 849px;
    height: 860px;
    background:
      radial-gradient(ellipse 250px 340px at 250px 360px, #e9edf1 0%, #c7d1da 45%, rgba(150,168,184,0) 100%),
      linear-gradient(180deg, var(--night-top) 0%, var(--night-mid) 50%, var(--mist) 80%, var(--paper) 100%);
  }
  .vertical {
    position: absolute;
    margin: 0;
    writing-mode: vertical-rl;
    text-orientation: mixed;
    white-space: nowrap;
  }
  .tcy { text-combine-upright: all; }
  .producer {
    left: 753px; top: 40px;
    font-family: "Yuji Syuku", serif;
    font-size: 27px;
    line-height: 1;
    color: var(--ink);
  }
  .title {
    left: 631px; top: 108px;
    font-family: "Yuji Syuku", serif;
    font-weight: 400;
    font-size: 118px;
    line-height: 1;
    letter-spacing: 8px;
    color: var(--ink);
  }
  .date {
    left: 552px; top: 88px;
    font-size: 56px;
    font-weight: 800;
    line-height: 1;
    color: var(--ink);
  }
  .venue {
    left: 467px; top: 270px;
    font-size: 40px;
    font-weight: 700;
    line-height: 1;
    color: var(--ink);
  }
  .time {
    left: 416px; top: 425px;
    font-size: 17px;
    font-weight: 700;
    line-height: 1;
    color: var(--ink);
  }
  .tagline {
    position: absolute;
    left: 40px; top: 838px;
    width: 580px;
    text-align: center;
    font-size: 20px;
    font-weight: 700;
    color: var(--teal);
    letter-spacing: 1px;
  }
  .lead {
    position: absolute;
    left: 40px; top: 893px;
    margin: 0;
    font-size: 20px;
    font-weight: 700;
    line-height: 2.3;
    color: var(--ink);
  }
  .credits {
    position: absolute;
    left: 40px; top: 1052px;
    width: 570px;
    margin: 0;
    font-size: 10.5px;
    line-height: 1.7;
    color: var(--ink-soft);
  }
  .prices {
    position: absolute;
    left: 40px; top: 1134px;
    margin: 0;
    font-size: 21px;
    font-weight: 700;
    color: var(--ink);
    white-space: nowrap;
  }
  .contact {
    position: absolute;
    left: 40px; top: 1165px;
    margin: 0;
    font-size: 21px;
    font-weight: 700;
    color: var(--ink);
    white-space: nowrap;
  }
  .contact span + span { margin-left: 40px; }
  .qr-slot {
    position: absolute;
    left: 798px; top: 1118px;
    width: 46px; height: 46px;
    background: var(--white);
  }
</style>
</head>
<body>
<div class="poster">
  <div class="key-visual" role="img" aria-label="綿帽子をかぶった白無垢の女性が狐面を手に持つ写真と、夜の青い霧に浮かぶ狐火"></div>

  <div class="vertical producer">桜綾音プロデュース〈狐の嫁入り・鷺娘 など〉</div>
  <h1 class="vertical title">星のまたたき公演</h1>
  <div class="vertical date"><span class="tcy">2023</span>年<span class="tcy">11</span>月<span class="tcy">25</span>日<span class="tcy">(土)</span></div>
  <div class="vertical venue">緑町公会堂</div>
  <div class="vertical time"><span class="tcy">17</span>時〜<span class="tcy">19</span>時（開場<span class="tcy">16</span>時半）</div>

  <div class="tagline">― 伝統芸能×障害者の美意識が融合する夢幻舞台 ―</div>

  <p class="lead">1000年続く白鶴院39代目による<br>平安時代の和琴、時空を超えるほら貝、謎の語り部、<br>妖艶日本舞踊・元歌舞伎役者の粋！狐行列は素敵な障害者たち！</p>

  <p class="credits">主催：一般社団法人 森のこだま<br>共催：一般社団法人 ハッピーステップ俱楽部<br>出演：桜綾音・藤波流清舟・村瀬健吾・KAZMO・紗弥・ハッピーステップ俱楽部（松田凛・北川原誠一・石塚美穂・原田翔・大西菜摘・桑原陽斗・長谷部千尋・川口結衣・三浦彩乃・柴田浩明・吉川みき・堀江ナオ）</p>

  <p class="prices">VIP席：10,000円／一般席（当日受付）：7,000円／一般席（前売）：6,000円</p>
  <p class="contact"><span>チケット申込先：TEL.00-000-000</span><span>お問合せ：00-000-000</span></p>
  <div class="qr-slot"></div>
</div>
</body>
</html>
```